Larkfield Rowhomes - Billboard design for our newly renovated townhome community

We have a 5' wide x 4' tall billboard at the entrance to our apartment community, that needs to have the acrylic insert replaced. It is a 2 sided sign, and we are planning to use the same image on both sides. We are called Larkfield Rowhomes, and have 48 townhomes that are all 2 bedroom, 1 1/2 bath. A few things we would like to get across on the signage: "Newly Renovated" "2 bed 1 1/2 bath" "Full size W/D in every home" " New Appliances" I've included our parent company's logo - this is the only image I could think of, but it might not be worth having it on the sign. We are in Colorado, so mountain theme could be nice and also sunshine/sun since we are called "Larkfield"

Industry/Entity Type

Apartment

Font styles to use
Sans Serif

Requirements
Must have
• Newly Renovated
2 bed 1 1/2 bath
Full size W/D in every home
Virtual Tours available
www.brambletonhomesco.example
855 - 413 - 9286
Nice to have
• We are located in Colorado - possibly mountain theme? Since our community is called "Larkfield Rowhomes" - anything bright with Sun / Sunshine might look really nice as well.

```html
<!DOCTYPE html>
<html lang="en">
<head>
<meta charset="utf-8">
<title>Larkfield Rowhomes – Entrance Billboard</title>
<link rel="stylesheet" href="https://fonts.googleapis.com/css2?family=Fredoka:wght@500;600;700&display=swap">
<style>
  :root {
    --navy: #1f3468;
    --navy-deep: #172a55;
    --sky-top: #d98f86;
    --sky-glow: #f6c79a;
    --sun: #fff7dc;
    --peak: #e7b08c;
    --forest: #2a3f72;
    --sand: #ecc891;
    --white: #ffffff;
    --ink: #111111;
    --house: #a9b6c4;
  }
  * { box-sizing: border-box; margin: 0; padding: 0; }
  html, body {
    width: 1200px; height: 1200px; overflow: hidden;
    background: #ffffff;
    font-family: "Fredoka", sans-serif;
  }
  .billboard {
    position: relative; width: 1200px; height: 1200px; overflow: hidden;
    background: var(--navy-deep);
  }
  .scene {
    position: absolute; inset: 0;
    background:
      radial-gradient(circle at 760px 230px, var(--sun) 0 40px, rgba(255,240,200,.75) 90px, rgba(246,199,154,0) 300px),
      linear-gradient(180deg, var(--sky-top) 0%, var(--sky-glow) 32%, var(--peak) 50%, #8a7f9a 62%, var(--forest) 74%, var(--navy-deep) 100%);
  }
  .edge-strip {
    position: absolute; left: 0; top: 0; width: 26px; height: 300px;
    background: var(--navy-deep);
  }
  .parent-brand {
    position: absolute; left: 26px; top: 0; width: 430px; height: 300px;
    background: var(--white);
    display: flex; align-items: center; justify-content: center;
  }
  .parent-brand__name {
    font-weight: 500; font-size: 40px; color: var(--navy);
  }
  .headline {
    position: absolute; left: 30px; top: 300px;
    color: var(--white); font-weight: 700; line-height: .95;
    text-transform: uppercase; letter-spacing: -2px;
    -webkit-text-stroke: 10px var(--ink); paint-order: stroke fill;
    text-shadow: 6px 6px 0 var(--ink);
    white-space: nowrap;
  }
  .headline__line { display: block; font-size: 160px; }
  .headline__line--second { margin-left: -14px; font-size: 172px; }
  .features {
    position: absolute; left: 20px; top: 650px;
    display: flex; align-items: flex-start; gap: 22px;
  }
  .feature-pill {
    height: 70px; padding: 0 22px;
    display: flex; align-items: center;
    border: 4px solid var(--sand); border-radius: 18px;
    background: var(--navy);
    color: var(--white); font-weight: 600; font-size: 38px;
    white-space: nowrap;
  }
  .feature-pill--laundry { margin-top: 22px; }
  .feature-note {
    position: absolute; left: 430px; top: 772px;
    color: var(--white); font-weight: 600; font-size: 42px;
    text-shadow: 3px 3px 0 var(--ink);
    white-space: nowrap;
  }
  .home-photo {
    position: absolute; left: 0; top: 860px; width: 280px; height: 340px;
    background: linear-gradient(180deg, #6e93c9 0%, var(--house) 55%, #8f8474 100%);
    border-top: 6px solid var(--sand);
  }
  .contact-band {
    position: absolute; left: 280px; top: 880px; right: 0; bottom: 0;
    background: var(--sand);
    padding: 40px 0 0 36px;
    color: var(--navy); font-weight: 700;
    overflow: hidden;
  }
  .contact-band__phone { font-size: 104px; line-height: 1; letter-spacing: 1px; white-space: nowrap; }
  .contact-band__web { font-size: 48px; font-weight: 600; line-height: 1.1; margin-top: 36px; white-space: nowrap; }
</style>
</head>
<body>
  <main class="billboard">
    <div class="scene" role="img" aria-label="Photo of snow-capped Colorado peaks at sunrise with a bright sun and pine forest below"></div>
    <div class="edge-strip"></div>

    <div class="parent-brand">
      <span class="parent-brand__name">Crestline Partners</span>
    </div>

    <h1 class="headline">
      <span class="headline__line">Newly</span>
      <span class="headline__line headline__line--second">Renovated</span>
    </h1>

    <div class="features">
      <div class="feature-pill feature-pill--rooms">2 bed 1 1/2 bath</div>
      <div class="feature-pill feature-pill--laundry">Full size W/D in every home</div>
    </div>
    <p class="feature-note">Virtual Tours Available</p>

    <div class="home-photo" role="img" aria-label="Photo of a renovated two-storey townhome exterior under blue sky"></div>

    <div class="contact-band">
      <div class="contact-band__phone">855 - 413 - 9286</div>
      <div class="contact-band__web">www.brambletonhomesco.example</div>
    </div>
  </main>
</body>
</html>
```